Ridgeway Fruit Depot Logo/Label Design

I am designing a blueberry label that will be placed on clam shells when the fruit is packed. The label will the company name "The Ridgeway Fruit Depot". It will also list Blueberries/Bleuets (Blueberries in French). It small print it would say Dist. By/Par The Ridgeway Fruit Depot, Corliss, GA 30874 USA. It would also list the package size. 1 US Dry Pint/1 Chopine Seche US 551 ml. I have provided some sample labels that other marketers use.

```html
<!DOCTYPE html>
<html lang="en">
<head>
<meta charset="UTF-8">
<title>The Ridgeway Fruit Depot – Blueberries Label</title>
<link rel="stylesheet" href="https://fonts.googleapis.com/css2?family=Source+Serif+4:opsz,wght@8..60,600;8..60,700&family=Source+Sans+3:wght@500&display=swap">
<style>
  :root {
    --paper: #f6f2e8;
    --navy: #13284f;
    --cream: #f5efe2;
    --berry-light: #5a7cc4;
    --berry-dark: #243d7d;
    --leaf: #5b9a3c;
    --flag-red: #c8343e;
    --flag-white: #f4f1ec;
    --flag-blue: #2c3f7c;
  }
  html, body {
    margin: 0;
    padding: 0;
    width: 800px;
    height: 1200px;
    overflow: hidden;
    background: var(--paper);
  }
  .label {
    position: relative;
    width: 800px;
    height: 1200px;
    color: var(--cream);
  }
  .label__oval {
    position: absolute;
    inset: 0;
  }
  .label__line {
    position: absolute;
    left: 0;
    width: 800px;
    margin: 0;
    text-align: center;
    line-height: 1;
    white-space: nowrap;
  }
  .brand {
    font-family: "Source Serif 4", Georgia, serif;
    font-weight: 700;
    letter-spacing: 0.02em;
  }
  .brand--small { top: 158px; font-size: 34px; }
  .brand--large { font-size: 62px; }
  .brand--line1 { top: 226px; }
  .brand--line2 { top: 301px; }
  .berry-art {
    position: absolute;
    left: 202px;
    top: 379px;
    width: 392px;
    height: 176px;
  }
  .product {
    font-family: "Source Serif 4", Georgia, serif;
    font-weight: 600;
    font-size: 108px;
    letter-spacing: -0.005em;
  }
  .product--en { top: 562px; }
  .product--fr { top: 673px; }
  .fine {
    font-family: "Source Sans 3", Arial, sans-serif;
    font-weight: 500;
    font-size: 27px;
  }
  .fine--dist1 { top: 802px; }
  .fine--dist2 { top: 841px; }
  .fine--size1 { top: 898px; }
  .fine--size2 { top: 939px; }
  .origin-flag {
    position: absolute;
    left: 348px;
    top: 991px;
    width: 104px;
    height: 64px;
  }
</style>
</head>
<body>
<main class="label">
  <svg class="label__oval" width="800" height="1200" viewBox="0 0 800 1200" aria-hidden="true">
    <ellipse cx="400" cy="601" rx="371" ry="501" fill="var(--navy)"/>
    <ellipse cx="400" cy="601" rx="360" ry="490" fill="none" stroke="var(--cream)" stroke-width="3"/>
  </svg>

  <p class="label__line brand brand--small">THE</p>
  <p class="label__line brand brand--large brand--line1">RIDGEWAY</p>
  <p class="label__line brand brand--large brand--line2">FRUIT DEPOT</p>

  <svg class="berry-art" viewBox="0 0 392 176" role="img" aria-label="Illustration of a cluster of blueberries with green leaves">
    <defs>
      <radialGradient id="berryTone" cx="45%" cy="40%" r="60%">
        <stop offset="0%" stop-color="var(--berry-light)"/>
        <stop offset="70%" stop-color="var(--berry-dark)"/>
        <stop offset="100%" stop-color="var(--leaf)"/>
      </radialGradient>
    </defs>
    <ellipse cx="196" cy="88" rx="194" ry="86" fill="url(#berryTone)"/>
  </svg>

  <h1 class="label__line product product--en">Blueberries</h1>
  <p class="label__line product product--fr" lang="fr">Bleuets</p>

  <p class="label__line fine fine--dist1">Dist. By/Par The Ridgeway Fruit Depot,</p>
  <p class="label__line fine fine--dist2">Corliss, GA 30874 USA</p>
  <p class="label__line fine fine--size1">1 US Dry Pint / 1 Chopine Séche</p>
  <p class="label__line fine fine--size2">US 551 ml</p>

  <svg class="origin-flag" viewBox="0 0 104 64" role="img" aria-label="United States flag indicating country of origin">
    <defs>
      <linearGradient id="flagTone" x1="0" y1="0" x2="1" y2="1">
        <stop offset="0%" stop-color="var(--flag-blue)"/>
        <stop offset="45%" stop-color="var(--flag-white)"/>
        <stop offset="100%" stop-color="var(--flag-red)"/>
      </linearGradient>
    </defs>
    <rect width="104" height="64" fill="url(#flagTone)"/>
  </svg>
</main>
</body>
</html>
```